Calloway needs a modernized design

We would like a modern update (that can be responsive) to our existing website. Attached are the two existing pages we would like new concepts of - our home page and a page about one of our locations.

Calloway is provides executive offices and virtual office services. Startups, law firms, and financial services are our primary clients. We would like a professional, clean design, leaning towards minimalist. We intend to greatly reduce/eliminate the long paragraphs of text.

Industry/Entity Type

Business Service

Number of Pages Required

2 page

Requirements
Must have
• A design that can be responsive
Nice to have
• Large image(s) on home page that rotate.

```html
<!DOCTYPE html>
<html lang="en">
<head>
<meta charset="utf-8">
<title>Calloway Business Centers</title>
<link href="https://fonts.googleapis.com/css2?family=Bitter:wght@400;700&family=Open+Sans:wght@400;600;700&display=swap" rel="stylesheet">
<style>
:root{
  --navy:#25356a;
  --navy-dark:#1d2b59;
  --ink:#333;
  --muted:#555;
  --ring:#dcdcdc;
  --grey:#6b6b6b;
  --white:#fff;
  --black:#151515;
  --link:#3f8fd8;
}
*{margin:0;padding:0;box-sizing:border-box}
html,body{width:1200px;height:2853px;overflow:hidden}
body{position:relative;background:var(--white);font-family:"Open Sans",Arial,sans-serif;color:var(--ink)}
.abs{position:absolute}
.serif{font-family:"Bitter",Georgia,serif}

/* header */
.site-header{position:absolute;left:0;top:0;width:1200px;height:112px}
.brand{position:absolute;left:48px;top:14px;display:flex;align-items:center;gap:12px}
.brand-mark{width:56px;height:56px;border-radius:50%;background:var(--navy)}
.brand-name{font-family:"Bitter",Georgia,serif;font-size:30px;color:var(--navy);font-weight:400;letter-spacing:1px}
.main-nav{position:absolute;left:420px;top:57px;display:flex;height:48px}
.main-nav a{display:block;padding:0 30px;line-height:48px;font-family:"Bitter",Georgia,serif;font-size:13px;letter-spacing:.5px;color:#222;text-decoration:none;text-transform:uppercase}
.main-nav a.active{background:var(--navy);color:var(--white);padding:0 26px}
.nav-rule{position:absolute;left:48px;top:104px;width:1104px;height:3px;background:#222}

/* hero */
.hero{position:absolute;left:0;top:120px;width:1200px;height:528px;background:linear-gradient(100deg,#eef0f4 0%,#c9ced9 40%,#6e7a96 70%,#35415f 100%)}
.hero-panel{position:absolute;left:48px;top:112px;width:502px;height:308px;background:rgba(255,255,255,.72);padding:30px 30px}
.hero-panel h1{font-weight:400;font-size:32px;color:#2a2a2a;letter-spacing:.5px;line-height:1.1}
.hero-panel h2{font-weight:700;font-size:46px;color:var(--navy);letter-spacing:1px;line-height:1.1;margin-top:4px}
.hero-panel p{font-size:14px;line-height:22px;color:#222;margin-top:14px;width:440px}
.btn{display:inline-block;font-size:13px;text-transform:uppercase;letter-spacing:.3px;text-decoration:none;text-align:center}
.btn-dark{margin-top:20px;border:2px solid #222;color:#222;padding:0 18px;line-height:36px}

/* services */
.service{position:absolute;top:686px;width:230px;text-align:center}
.service-ring{width:174px;height:174px;border-radius:50%;background:var(--ring);margin:0 auto;display:flex;align-items:center;justify-content:center}
.service-core{width:150px;height:150px;border-radius:50%;background:var(--navy);display:flex;align-items:center;justify-content:center}
.service-disc{width:108px;height:108px;border-radius:50%;background:var(--grey);display:flex;align-items:center;justify-content:center}
.service h3{font-family:"Bitter",Georgia,serif;font-weight:700;font-size:18px;line-height:22px;color:#222;margin-top:20px;letter-spacing:.5px}
.service .bar{width:58px;height:4px;background:#999;margin:8px auto 0}
.service .bar.on{background:var(--navy)}

/* why band */
.why{position:absolute;left:0;top:990px;width:1200px;height:613px;background:var(--navy)}
.why-title{position:absolute;left:0;top:28px;width:1200px;text-align:center;color:var(--white);font-family:"Bitter",Georgia,serif;font-weight:700;font-size:20px;line-height:29px;letter-spacing:.3px}
.pillar{position:absolute;top:140px;width:340px;text-align:center;color:var(--white)}
.pillar-photo{width:232px;height:232px;border-radius:50%;border:7px solid var(--white);margin:0 auto}
.pillar h3{font-family:"Bitter",Georgia,serif;font-weight:700;font-size:24px;margin-top:16px;letter-spacing:.5px}
.pillar p{font-size:13px;line-height:21px;margin-top:12px;height:86px}
.btn-light{margin-top:16px;border:1px solid var(--white);color:var(--white);padding:0 12px;line-height:30px;font-size:12px}

/* videos & news */
.section-title{font-family:"Bitter",Georgia,serif;font-size:34px;font-weight:400;color:#333}
.video{position:absolute;top:1737px;width:284px}
.video-thumb{position:relative;width:284px;height:183px;background:linear-gradient(180deg,#8b8e88,#5c5a52 70%,#3f3c37)}
.video-thumb .ctrl{position:absolute;left:0;bottom:0;width:100%;height:14px;background:rgba(0,0,0,.75)}
.video-thumb .play{position:absolute;left:114px;top:66px}
.video h4{font-family:Arial,Helvetica,sans-serif;font-weight:700;font-size:15px;color:#222;margin-top:18px}
.video p{font-family:Arial,Helvetica,sans-serif;font-size:13.5px;line-height:20px;color:#555;margin-top:8px}
.video .meta{display:flex;align-items:center;gap:6px;font-family:Arial,Helvetica,sans-serif;font-size:13px;color:#444;margin-top:14px}
.divider{position:absolute;left:703px;top:1672px;width:1px;height:405px;background:#bbb}
.news{position:absolute;left:733px;width:420px;display:flex;gap:22px}
.news-date{flex:none;width:96px;height:96px;border-radius:50%;border:5px solid var(--navy);display:flex;align-items:center;justify-content:center}
.news-date span{width:72px;height:72px;border-radius:50%;background:var(--navy);color:var(--white);font-family:Arial,Helvetica,sans-serif;font-weight:700;font-size:16px;line-height:19px;text-align:center;display:flex;align-items:center;justify-content:center}
.news h4{font-family:Arial,Helvetica,sans-serif;font-weight:700;font-size:15px;line-height:19px;color:#222;margin-top:4px}
.news p{font-family:Arial,Helvetica,sans-serif;font-size:16px;line-height:22px;color:#666;margin-top:4px}

/* experts */
.experts{position:absolute;left:0;top:2137px;width:1200px;height:420px;background:linear-gradient(90deg,#3a3a3a 0%,#4a4a4a 45%,#3c3d44 70%,#2e2f36 100%)}
.experts h2{position:absolute;left:0;top:48px;width:1200px;text-align:center;font-family:"Bitter",Georgia,serif;font-weight:400;font-size:34px;color:var(--white)}
.experts blockquote{position:absolute;left:140px;top:112px;width:920px;text-align:center;color:var(--white);font-size:14.5px;line-height:28px}
.experts cite{position:absolute;left:0;top:242px;width:1200px;text-align:center;color:var(--link);font-style:normal;font-size:14.5px}
.dots{position:absolute;left:542px;top:290px;display:flex;gap:6px}
.dots i{display:block;width:34px;height:5px;background:#ccc}
.dots i.on{background:var(--link)}
.btn-outline{position:absolute;left:518px;top:331px;width:152px;border:2px solid var(--white);color:var(--white);line-height:40px;font-size:13px}

/* footer */
.footer{position:absolute;left:0;top:2557px;width:1200px;height:246px;background:var(--navy);color:var(--white)}
.footer h3{font-weight:400;font-size:24px}
.footer ul{list-style:none}
.footer li{font-size:14.5px;line-height:27px}
.footer .sub{font-size:17px;color:#aab4d4;margin-top:12px}
.footer .small{font-size:13px;line-height:22px;margin-top:18px;width:270px}
.signup{display:flex;margin-top:18px}
.signup .field{width:172px;height:32px;background:var(--white);color:#888;font-size:12px;line-height:32px;padding-left:10px}
.signup .send{width:78px;height:32px;background:#e8e8e8;color:#999;font-size:12px;line-height:32px;text-align:center}
.socials{display:flex;gap:10px;margin-top:20px}
.socials i{display:block;width:38px;height:38px;border-radius:50%}
.foot-brand{display:flex;align-items:center;gap:10px;margin-top:24px;margin-left:10px}
.foot-brand .mark{width:48px;height:48px;border-radius:50%;background:#e9e3d3}
.foot-brand span{font-family:"Bitter",Georgia,serif;font-size:26px;color:#e9e3d3;letter-spacing:1px}
.copyright{position:absolute;left:0;top:2803px;width:1200px;height:50px;background:var(--black);color:var(--white);font-size:12px;line-height:50px;text-align:center;letter-spacing:.3px}
</style>
</head>
<body>

<header class="site-header">
  <div class="brand"><div class="brand-mark"></div><div class="brand-name">CALLOWAY</div></div>
  <nav class="main-nav">
    <a class="active" href="#">Home</a>
    <a href="#">Properties</a>
    <a href="#">Virtual Tours &amp; Videos</a>
    <a href="#">Photos</a>
    <a href="#">Broker Referrals</a>
  </nav>
  <div class="nav-rule"></div>
</header>

<section class="hero" role="img" aria-label="Business people reviewing documents with a pen at a desk">
  <div class="hero-panel">
    <h1>EXECUTIVE OFFICE SUITES</h1>
    <h2>ON LOW COST</h2>
    <p>Your company works hard to generate new business and stay competitive, so understanding how your products fare in the market, understanding customer buying habits, or even understanding where your sales force is failing, can give you the edge you need.</p>
    <a class="btn btn-dark" href="#">Read More</a>
  </div>
</section>

<section class="services">
  <div class="service" style="left:18px">
    <div class="service-ring"><div class="service-core"><div class="service-disc">
      <svg width="44" height="44" viewBox="0 0 44 44"><circle cx="22" cy="13" r="8" fill="#fff"/><path d="M6 40c0-10 7-15 16-15s16 5 16 15z" fill="#fff"/></svg>
    </div></div></div>
    <h3>Executive Office<br>Suites</h3><div class="bar on"></div>
  </div>
  <div class="service" style="left:247px">
    <div class="service-ring"><div class="service-core"><div class="service-disc">
      <svg width="54" height="44" viewBox="0 0 54 44"><circle cx="27" cy="10" r="6" fill="#fff"/><circle cx="12" cy="14" r="5" fill="#fff"/><circle cx="42" cy="14" r="5" fill="#fff"/><rect x="20" y="18" width="14" height="22" rx="3" fill="#fff"/><rect x="6" y="21" width="12" height="18" rx="3" fill="#fff"/><rect x="36" y="21" width="12" height="18" rx="3" fill="#fff"/></svg>
    </div></div></div>
    <h3>On-demand<br>Meeting Rooms</h3><div class="bar"></div>
  </div>
  <div class="service" style="left:486px">
    <div class="service-ring"><div class="service-core"><div class="service-disc">
      <svg width="52" height="46" viewBox="0 0 52 46"><rect x="4" y="2" width="44" height="28" fill="none" stroke="#fff" stroke-width="3"/><path d="M12 24l10-10 6 6 10-10" fill="none" stroke="#fff" stroke-width="2"/><circle cx="14" cy="38" r="4" fill="#fff"/><circle cx="26" cy="38" r="4" fill="#fff"/><circle cx="38" cy="38" r="4" fill="#fff"/></svg>
    </div></div></div>
    <h3>On-demand<br>Training Rooms</h3><div class="bar"></div>
  </div>
  <div class="service" style="left:715px">
    <div class="service-ring"><div class="service-core"><div class="service-disc">
      <svg width="48" height="46" viewBox="0 0 48 46"><circle cx="16" cy="18" r="7" fill="#fff"/><path d="M2 44c0-9 6-14 14-14s14 5 14 14z" fill="#fff"/><rect x="32" y="4" width="13" height="24" rx="2" fill="none" stroke="#fff" stroke-width="2.5"/><circle cx="38.5" cy="23" r="1.8" fill="#fff"/></svg>
    </div></div></div>
    <h3>Virtual Office<br>Solutions</h3><div class="bar"></div>
  </div>
  <div class="service" style="left:952px">
    <div class="service-ring"><div class="service-core"><div class="service-disc">
      <svg width="52" height="46" viewBox="0 0 52 46"><circle cx="15" cy="20" r="7" fill="#fff"/><path d="M2 44c0-9 6-14 13-14s13 5 13 14z" fill="#fff"/><rect x="28" y="4" width="22" height="16" fill="none" stroke="#fff" stroke-width="2.5"/><path d="M36 9l6 3-6 3z" fill="#fff"/></svg>
    </div></div></div>
    <h3>Video Conference<br>Solutions</h3><div class="bar"></div>
  </div>
</section>

<section class="why">
  <h2 class="why-title">Come See Why Smarter Companies are Choosing Calloway Business Centers' Dallas, Ft. Worth and<br>Houston Executive Office Suites, Virtual Offices, Meeting Rooms and Video Conferencing.</h2>
  <div class="pillar" style="left:43px">
    <div class="pillar-photo" role="img" aria-label="Hand touching a glowing digital network" style="background:radial-gradient(circle at 45% 45%,#dfe8f3,#6f8fb8 55%,#2b3f64)"></div>
    <h3>Value</h3>
    <p>Either you need Dallas/Ft. Worth Office Space, Dallas Executive Suites, Ft. Worth Executive Suites, Houston Office Space, Houston Executive Suites, or maybe you simply need a place to stop in and use an on-demand</p>
    <a class="btn btn-light" href="#">Read More</a>
  </div>
  <div class="pillar" style="left:438px">
    <div class="pillar-photo" role="img" aria-label="Woman thinking with colourful lines of ideas around her" style="background:radial-gradient(circle at 50% 55%,#8a7363,#c9c3b8 55%,#e3dfd8)"></div>
    <h3>Community</h3>
    <p>Companies that partner with Calloway share more than a prestigious address. They also share ideas and services. Our Executive Office Business Centers are places where savvy, growing companies</p>
    <a class="btn btn-light" href="#">Read More</a>
  </div>
  <div class="pillar" style="left:812px">
    <div class="pillar-photo" role="img" aria-label="Two colleagues working together at a desk" style="background:linear-gradient(135deg,#f2f2f2,#b7c7dc 50%,#5f7fa8)"></div>
    <h3>Service</h3>
    <p>Calloway Business Centers positions its management team in every one of its business centers - we operate with an open-door policy as a medium-sized company without all of the corporate bureaucracy and red tape.</p>
    <a class="btn btn-light" href="#">Read More</a>
  </div>
</section>

<h2 class="section-title abs" style="left:48px;top:1668px">Our Videos</h2>
<div class="video" style="left:48px">
  <div class="video-thumb" role="img" aria-label="Video still of a presenter wearing a headset">
    <svg class="play" width="56" height="48" viewBox="0 0 56 48"><path d="M20 12l20 12-20 12z" fill="#fff"/></svg>
    <div class="ctrl"></div>
  </div>
  <h4>Learn the language of love</h4>
  <p>Education is the process of facilitating learning. Knowledge, skills, values, beliefs, and habits of a...</p>
  <div class="meta"><svg width="18" height="18" viewBox="0 0 18 18"><circle cx="9" cy="10" r="7" fill="none" stroke="#333" stroke-width="1.8"/><path d="M9 6v4h3" fill="none" stroke="#333" stroke-width="1.6"/></svg>2015-07-13 &nbsp;<svg width="16" height="16" viewBox="0 0 16 16"><path d="M8 2c4 0 7 2.5 7 5.5S12 13 8 13l-4 2 1-3C2.5 11 1 9.5 1 7.5 1 4.5 4 2 8 2z" fill="none" stroke="#333" stroke-width="1.5"/></svg>(4) by marlow</div>
</div>
<div class="video" style="left:374px">
  <div class="video-thumb" role="img" aria-label="Video still of a presenter wearing a headset">
    <svg class="play" width="56" height="48" viewBox="0 0 56 48"><path d="M20 12l20 12-20 12z" fill="#fff"/></svg>
    <div class="ctrl"></div>
  </div>
  <h4>Learn the language of love</h4>
  <p>Education is the process of facilitating learning. Knowledge, skills, values, beliefs, and habits of a...</p>
  <div class="meta"><svg width="18" height="18" viewBox="0 0 18 18"><circle cx="9" cy="10" r="7" fill="none" stroke="#333" stroke-width="1.8"/><path d="M9 6v4h3" fill="none" stroke="#333" stroke-width="1.6"/></svg>2015-07-13 &nbsp;<svg width="16" height="16" viewBox="0 0 16 16"><path d="M8 2c4 0 7 2.5 7 5.5S12 13 8 13l-4 2 1-3C2.5 11 1 9.5 1 7.5 1 4.5 4 2 8 2z" fill="none" stroke="#333" stroke-width="1.5"/></svg>(4) by marlow</div>
</div>

<div class="divider"></div>

<h2 class="section-title abs" style="left:746px;top:1654px">Our News</h2>
<div class="news" style="top:1733px">
  <div class="news-date"><span>Nov<br>01</span></div>
  <div><h4>The Surprising Reason College Expensive</h4><p>Cras condimentum a elit eget sagittis. Ut dignissim sapien feugiat...</p></div>
</div>
<div class="news" style="top:1845px">
  <div class="news-date"><span>Nov<br>21</span></div>
  <div><h4>The Surprising Reason College Expensive</h4><p>Cras condimentum a elit eget sagittis. Ut dignissim sapien feugiat...</p></div>
</div>
<div class="news" style="top:1955px">
  <div class="news-date"><span>Nov<br>11</span></div>
  <div><h4>The Surprising Reason College Expensive</h4><p>Cras condimentum a elit eget sagittis. Ut dignissim sapien feugiat...</p></div>
</div>

<section class="experts" role="img" aria-label="Dimmed photo of a businessman in a suit">
  <h2>Ask Our Experts</h2>
  <blockquote>"Northway Software's reputation for extensive knowledge of business intelligence analytics has a well-founded basis. Partnering with them was a win-win from day one onward, repeatedly demonstrated by our teams working together in unified fashion to quickly identify and resolve technical issues while delivering highly valued solutions that solved difficult market problems. A solid talented group of professionals who are a pleasure to engage with."</blockquote>
  <cite>Dr. Alan Pierce, Vice President/General Manager - Analytics, Leading Healthcare IT Company</cite>
  <div class="dots"><i class="on"></i><i></i><i></i></div>
  <a class="btn btn-outline" href="#">Read More</a>
</section>

<footer class="footer">
  <div class="abs" style="left:86px;top:28px">
    <h3>Navigation Links</h3>
    <div style="display:flex;gap:100px;margin-top:16px">
      <ul><li>About Us</li><li>Contact Us</li><li>Forms</li><li>Testimonials</li><li>FAQs</li></ul>
      <ul><li>Careers</li><li>Furniture</li><li>Specials</li><li>Site Map</li><li>Privacy</li></ul>
    </div>
  </div>
  <div class="abs" style="left:496px;top:28px">
    <h3>Newsletter Letter</h3>
    <div class="sub">Sign up to our mailing list</div>
    <div class="small">Suspendisse tempus sodales neque, eget eleifend turpis tristique eu.</div>
    <div class="signup"><div class="field">Email</div><div class="send">Subscribe</div></div>
  </div>
  <div class="abs" style="left:879px;top:28px">
    <h3>Social Media</h3>
    <div class="socials">
      <i style="background:#3b5998" aria-label="Social link"></i>
      <i style="background:#1da1f2" aria-label="Social link"></i>
      <i style="background:#cc181e" aria-label="Social link"></i>
      <i style="background:#3f729b" aria-label="Social link"></i>
      <i style="background:#dd4b39" aria-label="Social link"></i>
    </div>
    <div class="foot-brand"><div class="mark"></div><span>CALLOWAY</span></div>
  </div>
</footer>
<div class="copyright">COPYRIGHT 2012 CALLOWAY BUSINESS CENTERS ALL RIGHTS RESERVED</div>

</body>
</html>
```